Lotvantage.com Webpage Design

Design Brief for lotvantage.com (Copy of Brief also in attached Word file)

Name of Website- lotvantage.com (existing logo and look & feel of website to be changed)

Logo - Finalised. The logo files are attached with the brief as “logo.jpeg”. The “Blue- Grey” version of the logo is for use on lighter backgrounds and the “Orange-White” version of the logo is for use on darker backgrounds. (A full Black version of the logo is also attached). Both versions may be used in different parts of the website. All attached files are in .png format.
Status - The website in functional and is undergoing user trials. However, we want to improve the look & feel of the website so at it seems
a. cotemporary,
b. Easy to Navigate
c. professional and
d. Vibrant.

Please visit ‘lotvantage.com’ to check out the website and its functionalities – please use it only as a reference for the features & functions to be provided, however the designer should use a ‘Free Hand’ in designing the composition of various parts of the webpage without getting too influenced by the existing design

Objective of the Website ‘lotvantage.com –
a. It is a portal focussed on listing of ‘Retail’ specific real-estate properties by developers, owners and realty brokers. The properties shall listed under the following four categories-
i. Retail Malls
ii. Shopping Complexes
iii. High-street shops
iv. Retail Warehouses
*refer lotvantage.com for better clarity

b. The abovementioned properties shall be listed either for ‘Sale’ or ‘rent\lease’ or both

c. Users shall visit the site in case they wish to acquire a retail \ shop space either on ‘sale’ or ‘rent’. These Users would be able to specify the ‘Search Criteria’ through the tool-bars provided on the website – the ‘Search Criteria’ shall comprise of ‘Type of space category’, ‘City’, ‘Locality’, transaction type ie ‘Rent \ Sale’ and ‘Area Range’

d. The main revenue model for the website shall be listing fee ( or advertising charges ) payable by those listing their properties on the website.

Three Main Pages of Website (lotvantage.com) that need to be designed -
a. Main Home Page (visit the web link - http://lotvantage.com/ ) - The main home page has the “Search Toolbar” for specifying of Search Criteria by the User. It shall also have the following features & functions-
i. Main Advertising Banner
ii. Featured Projects
iii. New Launches
iv. Toolbar with buttons – ‘Advertise with Us’, ‘Listings Alert’, ‘Lot Mavens’, ‘Advertiser Login’

b. Property Listings Page (visit the web link - http://lotvantage.com/gurgaon-in-india ) - The List of property options that match the Criteria specified by the ‘User’ get displayed on this page.

c. Property Detail Page - When the ‘User’ clicks on the “More….” Button on the ‘Property Listings Page’ (given in point b. above) the web page with the details of the property opens. (For Example – visit the web link - http://lotvantage.com/brevo-Shopping-Complex-brevo-quadrel-gurgaon-636 )

Note:- Please refer to attached ‘Shopping’ related images the designer may use them on the website to provide a look & feel of retail if required – either separately or rotate in a single window

Target Market(s)

Retailers & Investors looking for retail space, Real Estate Brokers, Developers

Industry/Entity Type

Advertising

Number of Pages Required

3 page

Requirements
Must have
• Refer to existing site lotvantage.com -- all the existing functionalities are a must have.
Nice to have
• The Designer may use the retail related images on the website if required for making it more vibrant. Refer attached images Shopping(1-6).jpg

```html
<!DOCTYPE html>
<html lang="en">
<head>
<meta charset="utf-8">
<title>Lotvantage.com – Retail Spaces for Sale &amp; Rent</title>
<link rel="stylesheet" href="https://fonts.googleapis.com/css2?family=Open+Sans:wght@400;600;700;800&display=swap">
<style>
:root{
  --blue:#1b97e6;
  --blue-dark:#0f7fca;
  --panel:#cfe5f5;
  --page:#eef1f4;
  --ink:#333a40;
  --muted:#7b8288;
  --line:#dde2e6;
  --ad:#5b5f63;
  --footer:#262829;
  --footer-bar:#1b1c1d;
}
*{box-sizing:border-box;margin:0;padding:0}
html,body{width:1200px;height:2685px;overflow:hidden}
body{font-family:"Open Sans",Arial,sans-serif;color:var(--ink);background:var(--page);position:relative;font-size:12px}
a{color:inherit;text-decoration:none}

/* header */
.site-header{position:absolute;left:0;top:0;width:1200px;height:121px;background:#fff;border-top:4px solid var(--blue)}
.top-strip{position:absolute;top:8px;left:470px;display:flex;align-items:center;gap:10px;font-size:11px;color:var(--blue)}
.fake-select{border:1px solid var(--line);height:22px;width:160px;font-size:10px;color:var(--muted);padding:3px 6px;background:#fff}
.connect{position:absolute;top:12px;left:819px;display:flex;align-items:center;gap:8px;font-size:11px;color:var(--blue)}
.connect .dot{width:14px;height:14px;border-radius:50%;background:#9aa3aa}
.brand{position:absolute;left:134px;top:52px;display:flex;align-items:center;gap:10px}
.brand .mark{width:30px;height:30px;border-radius:50%;background:var(--blue)}
.brand .name{font-size:30px;font-weight:700;color:#2b3a47;letter-spacing:-.5px}
.header-search{position:absolute;left:462px;top:62px;display:flex}
.header-search .field{width:250px;height:34px;border:1px solid var(--line);font-size:11px;color:var(--muted);padding:9px 10px}
.header-search .go{width:34px;height:34px;background:var(--blue);display:flex;align-items:center;justify-content:center}
.btn-login,.btn-register{position:absolute;top:62px;height:34px;font-size:11px;font-weight:700;color:#fff;display:flex;align-items:center;justify-content:center;text-transform:uppercase}
.btn-login{left:787px;width:126px;background:var(--blue)}
.btn-register{left:924px;width:142px;background:#3a3f44}

/* hero */
.hero{position:absolute;left:0;top:121px;width:1200px;height:357px;
  background:linear-gradient(180deg,#1d2a4a 0%,#3a4a70 35%,#7a5a48 70%,#c88a3e 100%)}

/* search */
.format-tab{position:absolute;left:140px;top:478px;width:222px;height:40px;background:var(--panel);display:flex;align-items:center;gap:14px;padding-left:10px;font-size:12px;font-weight:600;color:var(--blue)}
.format-tab .ico{width:28px;height:28px;background:var(--blue);display:flex;align-items:center;justify-content:center}
.format-tab .q{width:15px;height:15px;border:1px solid var(--blue);border-radius:50%;font-size:10px;display:flex;align-items:center;justify-content:center}
.search-panel{position:absolute;left:130px;top:518px;width:940px;height:228px;background:var(--panel)}
.check{position:absolute;top:24px;display:flex;align-items:center;gap:8px;font-size:11px;color:var(--ink)}
.check .box{width:13px;height:13px;border:1px solid #8aa;background:#fff}
.check .box.on{background:var(--blue);border-color:var(--blue)}
.field-label{position:absolute;top:80px;font-size:11px;color:var(--ink)}
.select{position:absolute;top:110px;height:30px;width:200px;background:#fff;border:1px solid #bcd3e3;font-size:10px;color:var(--muted);padding:8px 10px}
.select::after{content:"";position:absolute;right:10px;top:12px;border:4px solid transparent;border-top-color:#555}
.btn-search{position:absolute;left:26px;top:159px;width:121px;height:35px;background:var(--blue);color:#fff;font-weight:700;font-size:12px;display:flex;align-items:center;justify-content:center;gap:8px}
.city-tags{position:absolute;left:246px;top:166px;display:flex;gap:7px}
.city-tags span{background:var(--blue);color:#fff;font-size:9px;padding:5px 0;width:74px;text-align:center}

/* main */
.main{position:absolute;left:130px;top:746px;width:940px;height:1209px;background:#fff}
.section-title{position:absolute;font-size:21px;font-weight:700;color:var(--blue);display:flex;align-items:center;gap:14px}
.section-title::after{content:"";height:3px;background:#e6eaed;flex:1}
.card{position:absolute;width:212px;border:1px solid var(--line);background:#fff}
.card .photo{height:100px;position:relative}
.card .tag{position:absolute;right:0;bottom:0;background:var(--blue);color:#fff;font-size:9px;padding:3px 8px}
.card .body{padding:8px 10px 10px}
.card .title{font-size:11px;font-weight:700;color:var(--blue);text-transform:uppercase;display:flex;gap:6px;align-items:center}
.card .loc{font-size:10px;color:var(--ink);display:flex;gap:6px;align-items:center;margin-top:4px}
.card .desc{font-size:9.5px;line-height:1.45;color:var(--muted);margin-top:6px;height:42px;overflow:hidden}
.card .more{font-size:10px;font-weight:700;color:var(--ink);margin-top:6px}
.pin{width:8px;height:11px;flex:none}
.ph-a{background:linear-gradient(135deg,#b48b5c,#6d5a48)}
.ph-b{background:linear-gradient(135deg,#d6a66a,#8b6a44)}
.ph-c{background:linear-gradient(135deg,#e05a4a,#f0b44a)}
.ph-d{background:linear-gradient(135deg,#f4c66a,#b3a38a)}
.ph-e{background:linear-gradient(135deg,#8e9aa6,#c7b59a)}
.ph-f{background:linear-gradient(135deg,#6a7a86,#a8a08e)}

.pager{position:absolute;left:271px;top:645px;display:flex;gap:6px}
.pager span{width:22px;height:22px;border:1px solid var(--line);font-size:10px;display:flex;align-items:center;justify-content:center;color:var(--muted)}
.pager span.on{background:var(--blue);color:#fff;border-color:var(--blue)}

.side-box{position:absolute;left:716px;width:198px;height:108px;background:var(--blue);color:#fff;display:flex;flex-direction:column;align-items:center;justify-content:center;gap:12px;font-size:11px;font-weight:700;text-transform:uppercase}
.editor-title{position:absolute;left:716px;top:424px;font-size:17px;font-weight:700;color:var(--blue)}
.editor-box{position:absolute;left:716px;top:454px;width:198px;height:169px;border:1px solid var(--line);padding:12px;font-size:10px;line-height:1.55;color:var(--ink)}
.read-more{position:absolute;left:716px;top:644px;font-size:10px;font-weight:700;color:var(--blue)}

.latest .card{width:200px}
.arrow{position:absolute;width:22px;height:26px;background:var(--blue);display:flex;align-items:center;justify-content:center}
.ad-space{position:absolute;left:26px;top:1058px;width:888px;height:121px;background:var(--ad);border:1px solid #444;color:#fff;font-size:22px;font-weight:700;display:flex;align-items:center;justify-content:center}

/* subscribe */
.subscribe{position:absolute;left:0;top:1955px;width:1200px;height:402px;background:linear-gradient(180deg,#2aa3ec,#1b8fdc);color:#fff;text-align:center}
.subscribe .env{position:absolute;left:0;top:78px;width:1200px;display:flex;justify-content:center;align-items:center;gap:14px}
.subscribe .env::before,.subscribe .env::after{content:"";width:70px;height:1px;background:rgba(255,255,255,.6)}
.subscribe h2{position:absolute;top:142px;width:1200px;font-size:30px;font-weight:700;letter-spacing:.5px}
.subscribe p{position:absolute;top:206px;width:1200px;font-size:12px}
.sub-form{position:absolute;left:156px;top:266px;display:flex;gap:10px}
.sub-form .in{height:34px;background:#fff;color:var(--muted);font-size:11px;padding:10px 12px;text-align:left}
.sub-form .btn{height:34px;width:126px;background:#fff;color:var(--blue);font-weight:700;font-size:11px;display:flex;align-items:center;justify-content:center}

/* footer */
.site-footer{position:absolute;left:0;top:2357px;width:1200px;height:288px;background:var(--footer);color:#c9cdd0}
.foot-brand{position:absolute;left:134px;top:52px;display:flex;align-items:center;gap:8px}
.foot-brand .mark{width:22px;height:22px;border-radius:50%;background:#fff}
.foot-brand .name{font-size:22px;font-weight:700;color:#fff}
.foot-about{position:absolute;left:134px;top:120px;width:350px;font-size:10px;line-height:1.6}
.foot-about .more{color:var(--blue);font-weight:700;display:block;margin-top:4px}
.foot-head{position:absolute;top:58px;font-size:15px;font-weight:700;color:#fff}
.foot-list{position:absolute;top:110px;list-style:none;font-size:10.5px;line-height:2.4}
.foot-list li::before{content:"› ";color:#888}
.contact{position:absolute;left:846px;top:110px;font-size:10.5px;line-height:1.6}
.contact div{display:flex;gap:8px;margin-bottom:10px}
.footer-bar{position:absolute;left:0;top:2645px;width:1200px;height:40px;background:var(--footer-bar);color:#aab;font-size:10px}
.footer-bar .copy{position:absolute;left:134px;top:14px}
.footer-bar .legal{position:absolute;right:134px;top:14px;display:flex;gap:24px}
</style>
</head>
<body>

<header class="site-header">
  <div class="top-strip">
    <svg width="10" height="13" viewBox="0 0 10 13"><path d="M5 0a5 5 0 0 0-5 5c0 4 5 8 5 8s5-4 5-8a5 5 0 0 0-5-5z" fill="#1b97e6"/><circle cx="5" cy="5" r="2" fill="#fff"/></svg>
    <span>Find your location</span>
    <div class="fake-select">Allahabad</div>
  </div>
  <div class="connect">
    <span>Connect with us</span>
    <span class="dot"></span><span class="dot"></span><span class="dot"></span><span class="dot"></span><span class="dot"></span>
  </div>
  <div class="brand"><span class="mark"></span><span class="name">Lotvantage</span></div>
  <div class="header-search">
    <div class="field">Enter Project Name or Developer's Name</div>
    <div class="go"><svg width="14" height="14" viewBox="0 0 14 14"><circle cx="6" cy="6" r="4.5" stroke="#fff" stroke-width="2" fill="none"/><path d="M9.5 9.5L13 13" stroke="#fff" stroke-width="2"/></svg></div>
  </div>
  <a class="btn-login">Advertiser Login</a>
  <a class="btn-register">Advertiser Register</a>
</header>

<div class="hero" role="img" aria-label="Banner photo of a busy city shopping street lit up at night"></div>

<div class="format-tab">
  <span class="ico"><svg width="14" height="14" viewBox="0 0 14 14"><circle cx="6" cy="6" r="4.5" stroke="#fff" stroke-width="2" fill="none"/><path d="M9.5 9.5L13 13" stroke="#fff" stroke-width="2"/></svg></span>
  Select Retail Format <span class="q">?</span>
</div>

<section class="search-panel">
  <div class="check" style="left:26px"><span class="box on"></span>Retails Malls</div>
  <div class="check" style="left:246px"><span class="box"></span>Shopping Complex</div>
  <div class="check" style="left:482px"><span class="box"></span>High Street Shops</div>
  <div class="check" style="left:716px"><span class="box"></span>Retail Warehouses</div>

  <div class="field-label" style="left:26px">Sale or Rent or Both -</div>
  <div class="field-label" style="left:246px">Select City -</div>
  <div class="field-label" style="left:482px">Select Locality / Micro - Market -</div>
  <div class="field-label" style="left:716px">Enter Keywords -</div>

  <div class="select" style="left:26px">- Select -</div>
  <div class="select" style="left:246px;width:210px">- Select -</div>
  <div class="select" style="left:482px">- Select -</div>
  <div class="select" style="left:716px;width:198px">Name of Projects, Developers</div>

  <a class="btn-search">SEARCH <svg width="12" height="10" viewBox="0 0 12 10"><path d="M0 5h10M6 1l4 4-4 4" stroke="#fff" stroke-width="2" fill="none"/></svg></a>
  <div class="city-tags">
    <span>Bangalore</span><span>Chennai</span><span>Greater Noida</span><span>Gurgaon</span><span>Hyderabad</span><span>Jaipur</span><span>Kolkata</span><span>Mumbai</span>
  </div>
</section>

<main class="main">
  <h2 class="section-title" style="left:26px;top:36px;width:668px">Featured Projects</h2>

  <article class="card" style="left:26px;top:94px">
    <div class="photo ph-a" role="img" aria-label="Photo of a shopping complex interior"><span class="tag">Shopping Complex</span></div>
    <div class="body">
      <div class="title"><svg class="pin" viewBox="0 0 10 13"><path d="M5 0a5 5 0 0 0-5 5c0 4 5 8 5 8s5-4 5-8a5 5 0 0 0-5-5z" fill="#1b97e6"/></svg>Meridian</div>
      <div class="loc"><svg class="pin" viewBox="0 0 10 13"><path d="M5 0a5 5 0 0 0-5 5c0 4 5 8 5 8s5-4 5-8a5 5 0 0 0-5-5z" fill="#7b8288"/></svg>Gujarat, Surat, Athwa</div>
      <p class="desc">Kavira Developers presents sustainable modern retail cum office complexes, developed with care for smart buyers.</p>
      <div class="more">View The Listing ▸</div>
    </div>
  </article>

  <article class="card" style="left:254px;top:94px">
    <div class="photo ph-b" role="img" aria-label="Photo of a high street shopping arcade"><span class="tag">Shopping Complex</span></div>
    <div class="body">
      <div class="title"><svg class="pin" viewBox="0 0 10 13"><path d="M5 0a5 5 0 0 0-5 5c0 4 5 8 5 8s5-4 5-8a5 5 0 0 0-5-5z" fill="#1b97e6"/></svg>Ashbury 81 High Street</div>
      <div class="loc"><svg class="pin" viewBox="0 0 10 13"><path d="M5 0a5 5 0 0 0-5 5c0 4 5 8 5 8s5-4 5-8a5 5 0 0 0-5-5z" fill="#7b8288"/></svg>Sector 81, Faridabad</div>
      <p class="desc">100 meters away from Faridabad's most affluent residential sectors 14-17. At the absolute entrance of the city.</p>
      <div class="more">View The Listing ▸</div>
    </div>
  </article>

  <article class="card" style="left:482px;top:94px">
    <div class="photo ph-c" role="img" aria-label="Photo of a bright retail mall atrium"><span class="tag">Retail Malls</span></div>
    <div class="body">
      <div class="title"><svg class="pin" viewBox="0 0 10 13"><path d="M5 0a5 5 0 0 0-5 5c0 4 5 8 5 8s5-4 5-8a5 5 0 0 0-5-5z" fill="#1b97e6"/></svg>Crestline 24K</div>
      <div class="loc"><svg class="pin" viewBox="0 0 10 13"><path d="M5 0a5 5 0 0 0-5 5c0 4 5 8 5 8s5-4 5-8a5 5 0 0 0-5-5z" fill="#7b8288"/></svg>Sohna Road, Gurgaon</div>
      <p class="desc">Crestline 24K, our most promising mixed-use commercial project spread across 1.76 hectares, features retail.</p>
      <div class="more">View The Listing ▸</div>
    </div>
  </article>

  <article class="card" style="left:26px;top:355px">
    <div class="photo ph-d" role="img" aria-label="Photo of shoppers carrying bags"><span class="tag">Retail Malls</span></div>
    <div class="body">
      <div class="title"><svg class="pin" viewBox="0 0 10 13"><path d="M5 0a5 5 0 0 0-5 5c0 4 5 8 5 8s5-4 5-8a5 5 0 0 0-5-5z" fill="#1b97e6"/></svg>Harbor Mall</div>
      <div class="loc"><svg class="pin" viewBox="0 0 10 13"><path d="M5 0a5 5 0 0 0-5 5c0 4 5 8 5 8s5-4 5-8a5 5 0 0 0-5-5z" fill="#7b8288"/></svg>Tagore Garden, New Delhi</div>
      <p class="desc">Shopping never goes out of fashion. At Harbor it is a shopping, entertainment and leisure destination.</p>
      <div class="more">View The Listing ▸</div>
    </div>
  </article>

  <article class="card" style="left:254px;top:355px">
    <div class="photo ph-e" role="img" aria-label="Photo of a galleria shopping complex"><span class="tag">Shopping Complex</span></div>
    <div class="body">
      <div class="title"><svg class="pin" viewBox="0 0 10 13"><path d="M5 0a5 5 0 0 0-5 5c0 4 5 8 5 8s5-4 5-8a5 5 0 0 0-5-5z" fill="#1b97e6"/></svg>Northgate Galleria 91</div>
      <div class="loc"><svg class="pin" viewBox="0 0 10 13"><path d="M5 0a5 5 0 0 0-5 5c0 4 5 8 5 8s5-4 5-8a5 5 0 0 0-5-5z" fill="#7b8288"/></svg>Golf Course Road, Gurgaon</div>
      <p class="desc">Imagine a place where all you could ask for is already available. A place where work-life has a new rhythm.</p>
      <div class="more">View The Listing ▸</div>
    </div>
  </article>

  <article class="card" style="left:482px;top:355px">
    <div class="photo ph-f" role="img" aria-label="Photo of a mall food court"><span class="tag">Retail Malls</span></div>
    <div class="body">
      <div class="title"><svg class="pin" viewBox="0 0 10 13"><path d="M5 0a5 5 0 0 0-5 5c0 4 5 8 5 8s5-4 5-8a5 5 0 0 0-5-5z" fill="#1b97e6"/></svg>Tidal One</div>
      <div class="loc"><svg class="pin" viewBox="0 0 10 13"><path d="M5 0a5 5 0 0 0-5 5c0 4 5 8 5 8s5-4 5-8a5 5 0 0 0-5-5z" fill="#7b8288"/></svg>Sector 18, Noida</div>
      <p class="desc">Tidal One is all set to be a stable landmark that redefines retail experience and offers an enviable mix.</p>
      <div class="more">View The Listing ▸</div>
    </div>
  </article>

  <div class="pager"><span class="on">1</span><span>2</span><span>3</span></div>

  <a class="side-box" style="top:41px">
    <svg width="34" height="34" viewBox="0 0 34 34"><rect x="3" y="5" width="28" height="20" rx="2" stroke="#fff" stroke-width="2" fill="none"/><path d="M12 29h10M17 25v4" stroke="#fff" stroke-width="2"/></svg>
    Advertise With Us
  </a>
  <a class="side-box" style="top:164px">
    <svg width="30" height="34" viewBox="0 0 30 34"><path d="M15 3c-6 0-9 5-9 10v8l-3 4h24l-3-4v-8c0-5-3-10-9-10z" stroke="#fff" stroke-width="2" fill="none"/><path d="M11 29a4 4 0 0 0 8 0" stroke="#fff" stroke-width="2" fill="none"/></svg>
    Listing Alerts
  </a>
  <a class="side-box" style="top:288px">
    <svg width="34" height="34" viewBox="0 0 34 34"><path d="M6 11h22l-2 18H8z" stroke="#fff" stroke-width="2" fill="none"/><path d="M12 11V8a5 5 0 0 1 10 0v3" stroke="#fff" stroke-width="2" fill="none"/></svg>
    Lot Mavens
  </a>
  <h3 class="editor-title">Editor's Choice</h3>
  <div class="editor-box">A "Select" Listing of Retail Properties Handpicked by our Editors based on their own positive evaluation on parameters &amp; attributes such as Design Concept, Location, Developer, Success Potential. So Read On to Check Out for yourself!</div>
  <a class="read-more">READ MORE ›</a>

  <h2 class="section-title" style="left:26px;top:702px;width:888px">Latest Projects</h2>

  <div class="latest">
    <a class="arrow" style="left:15px;top:873px"><svg width="8" height="12" viewBox="0 0 8 12"><path d="M7 1L2 6l5 5" stroke="#fff" stroke-width="2" fill="none"/></svg></a>
    <a class="arrow" style="left:912px;top:873px"><svg width="8" height="12" viewBox="0 0 8 12"><path d="M1 1l5 5-5 5" stroke="#fff" stroke-width="2" fill="none"/></svg></a>

    <article class="card" style="left:45px;top:766px">
      <div class="photo ph-b" role="img" aria-label="Photo of a retail mall interior"><span class="tag">Retail Malls</span></div>
      <div class="body">
        <div class="title"><svg class="pin" viewBox="0 0 10 13"><path d="M5 0a5 5 0 0 0-5 5c0 4 5 8 5 8s5-4 5-8a5 5 0 0 0-5-5z" fill="#1b97e6"/></svg>Harbor Mall</div>
        <div class="loc"><svg class="pin" viewBox="0 0 10 13"><path d="M5 0a5 5 0 0 0-5 5c0 4 5 8 5 8s5-4 5-8a5 5 0 0 0-5-5z" fill="#7b8288"/></svg>Tagore Garden, New Delhi</div>
        <p class="desc">Shopping never goes out of fashion. At Harbor it is a shopping, entertainment and leisure...</p>
        <div class="more">View The Listing ▸</div>
      </div>
    </article>
    <article class="card" style="left:263px;top:766px">
      <div class="photo ph-d" role="img" aria-label="Photo of shoppers with bags"><span class="tag">Retail Malls</span></div>
      <div class="body">
        <div class="title"><svg class="pin" viewBox="0 0 10 13"><path d="M5 0a5 5 0 0 0-5 5c0 4 5 8 5 8s5-4 5-8a5 5 0 0 0-5-5z" fill="#1b97e6"/></svg>Harbor Mall</div>
        <div class="loc"><svg class="pin" viewBox="0 0 10 13"><path d="M5 0a5 5 0 0 0-5 5c0 4 5 8 5 8s5-4 5-8a5 5 0 0 0-5-5z" fill="#7b8288"/></svg>Tagore Garden, New Delhi</div>
        <p class="desc">Shopping never goes out of fashion. At Harbor it is a shopping, entertainment and leisure...</p>
        <div class="more">View The Listing ▸</div>
      </div>
    </article>
    <article class="card" style="left:481px;top:766px">
      <div class="photo ph-c" role="img" aria-label="Photo of a group of shoppers"><span class="tag">Retail Malls</span></div>
      <div class="body">
        <div class="title"><svg class="pin" viewBox="0 0 10 13"><path d="M5 0a5 5 0 0 0-5 5c0 4 5 8 5 8s5-4 5-8a5 5 0 0 0-5-5z" fill="#1b97e6"/></svg>Harbor Mall</div>
        <div class="loc"><svg class="pin" viewBox="0 0 10 13"><path d="M5 0a5 5 0 0 0-5 5c0 4 5 8 5 8s5-4 5-8a5 5 0 0 0-5-5z" fill="#7b8288"/></svg>Tagore Garden, New Delhi</div>
        <p class="desc">Shopping never goes out of fashion. At Harbor it is a shopping, entertainment and leisure...</p>
        <div class="more">View The Listing ▸</div>
      </div>
    </article>
    <article class="card" style="left:699px;top:766px">
      <div class="photo ph-a" role="img" aria-label="Photo of shoppers browsing a store"><span class="tag">Retail Malls</span></div>
      <div class="body">
        <div class="title"><svg class="pin" viewBox="0 0 10 13"><path d="M5 0a5 5 0 0 0-5 5c0 4 5 8 5 8s5-4 5-8a5 5 0 0 0-5-5z" fill="#1b97e6"/></svg>Harbor Mall</div>
        <div class="loc"><svg class="pin" viewBox="0 0 10 13"><path d="M5 0a5 5 0 0 0-5 5c0 4 5 8 5 8s5-4 5-8a5 5 0 0 0-5-5z" fill="#7b8288"/></svg>Tagore Garden, New Delhi</div>
        <p class="desc">Shopping never goes out of fashion. At Harbor it is a shopping, entertainment and leisure...</p>
        <div class="more">View The Listing ▸</div>
      </div>
    </article>
  </div>

  <div class="ad-space">Space for ADD</div>
</main>

<section class="subscribe">
  <div class="env"><svg width="30" height="22" viewBox="0 0 30 22"><rect x="1" y="1" width="28" height="20" stroke="#fff" stroke-width="2" fill="none"/><path d="M1 1l14 11L29 1" stroke="#fff" stroke-width="2" fill="none"/></svg></div>
  <h2>SUBSCRIBE OUR LISTING ALERTS !</h2>
  <p>Subscribe for Fortnightly Email update on New Listings @ Lotvantage</p>
  <div class="sub-form">
    <div class="in" style="width:236px">Enter your Email Address</div>
    <div class="in" style="width:236px">Select Retail Format</div>
    <div class="in" style="width:236px">Select Cities of interest</div>
    <div class="btn">SUBSCRIBE NOW</div>
  </div>
</section>

<footer class="site-footer">
  <div class="foot-brand"><span class="mark"></span><span class="name">Lotvantage</span></div>
  <p class="foot-about">Lotvantage.com is a Specialized Web based platform for Retail Space, featuring properties across India under various formats such as Retail Malls, Shopping Complexes, High street Shops. Also featured are Retail Warehouses which provide the logistic back-end for the retail business. Lotvantage.com is sorted by category of users as follows.<span class="more">Read More ›</span></p>

  <h4 class="foot-head" style="left:534px">Quick Navigation</h4>
  <ul class="foot-list" style="left:546px"><li>About Us</li><li>Contact Us</li><li>Site Map</li></ul>
  <ul class="foot-list" style="left:690px"><li>Retail Malls</li><li>Shopping Complex</li><li>High Street Shops</li><li>Retail Warehouses</li></ul>

  <h4 class="foot-head" style="left:846px">Contact With Us</h4>
  <div class="contact">
    <div><svg width="10" height="13" viewBox="0 0 10 13"><path d="M5 0a5 5 0 0 0-5 5c0 4 5 8 5 8s5-4 5-8a5 5 0 0 0-5-5z" fill="#1b97e6"/></svg><span>Marlowe House<br>Plot 27, 3rd Floor<br>Kestrel Park, Pune - 411000</span></div>
    <div><svg width="12" height="12" viewBox="0 0 12 12"><path d="M2 1l3 0 1 3-2 1a7 7 0 0 0 3 3l1-2 3 1v3c-6 0-10-4-10-10z" fill="#1b97e6"/></svg><span>000 - 000 - 0000</span></div>
  </div>
</footer>
<div class="footer-bar">
  <span class="copy">Copyright © 2015 Marlowe Retail Group. All rights reserved.</span>
  <span class="legal"><a>Privacy Policy</a><a>Terms of Use</a></span>
</div>

</body>
</html>
```